Yard Sign Manufacturing Company Needs a Website Design

We manufacture a variety of products including Lawnmark and would like to develop a stand alone website to cater to this business unit.

Competitor sites:
https://www.plakrova.com/yard-signs/
http://www.tavlune.com/

A few things to keep in mind/ elements we like from the competitors sites:
1) We do offer design services if someone dones not have a design

2) We would like the user to have the option to either select a template (based on industry: political, real estate, etc) or upload their own file

3) the site will focus on Lawnmark exclusively

4) Pricing, turn times, and ease of use seem to be the biggest factors in selecting a manufacturer

5) User experience/ flow is very important to us. We would like someone to be able to move forward with their sign selection/creation within the first click.

I like the "post a project" feel of mokrastudio.
Also, brelvato.com does a nice job of making it easy for the user to complete project with just a few clicks.

Pages I would like designed are the #1) homepage (prefer user to select whether to upload their own design or a template) #2) design page/upload page #3) checkout page

Target Market(s)

consumers of Lawnmark

Industry/Entity Type

Business

Number of Pages Required

3 page

Colors
0455a3
33a6d7
d0dfed

Requirements
Must have
• Element for user to upload their own design
• Element for users select a template -preferably sorted by industry
• Element for user to modify selected template for example - (https://www.quimbelorap.com/EditTool.aspx?T=9A1736281F03928475610B2C3D4E5F6A7B8C9D0E1F2A3B3C&S=2&M=1&CID=8827)
Nice to have
• minimal clicks to move forward with sign project

```html
<!DOCTYPE html>
<html lang="en">
<head>
<meta charset="utf-8">
<title>Lawnmark – Custom Signs</title>
<link rel="stylesheet" href="https://fonts.googleapis.com/css2?family=Open+Sans:ital,wght@0,300;0,400;0,600;0,700;0,800;1,400&display=swap">
<style>
:root{
  --blue:#0455a3;
  --sky:#33a6d7;
  --pale:#d0dfed;
  --orange:#f5a623;
  --text:#444;
  --muted:#777;
  --line:#d9d9d9;
  --gray-band:#eeeeee;
  --row-alt:#e4e4e4;
}
*{box-sizing:border-box;margin:0;padding:0}
html,body{width:1200px;height:2466px;overflow:hidden}
body{position:relative;font-family:'Open Sans',Arial,sans-serif;color:var(--text);background:#fff;font-size:12px}
a{color:inherit;text-decoration:none}
.abs{position:absolute}

/* header */
.topbar{left:0;top:0;width:1200px;height:72px;background:var(--blue)}
.brand{left:99px;top:18px;color:#fff;font-size:27px;font-weight:700;letter-spacing:.5px}
.search-btn{left:571px;top:17px;width:37px;height:37px;border-radius:50%;background:var(--sky)}
.search-btn svg{position:absolute;left:10px;top:10px}
.user-nav{left:635px;top:27px;display:flex;gap:28px;color:#fff;font-size:12px}
.user-nav span::after{content:" ⌄";font-size:10px}
.cart{left:969px;top:27px;color:#fff;font-size:12px;display:flex;gap:6px;align-items:center}

.mainnav{left:0;top:72px;width:1200px;height:37px;background:var(--sky)}
.mainnav ul{position:absolute;left:99px;width:1002px;top:0;height:37px;display:flex;list-style:none;border-left:1px solid rgba(255,255,255,.35)}
.mainnav li{flex:1;color:#fff;font-size:11.5px;text-align:center;line-height:37px;border-right:1px solid rgba(255,255,255,.35);text-transform:uppercase}

/* hero */
.hero{left:99px;top:109px;width:1002px;height:393px;overflow:hidden}
.hero-photo{position:absolute;inset:0;background:linear-gradient(100deg,#1d1f22 0%,#26282b 31%,#6e5f4f 36%,#b9a78f 52%,#c9c3b8 70%,#8e8a80 100%)}
.hero-copy{position:absolute;left:0;top:0;width:326px;height:393px;text-align:center;color:#fff}
.seal{position:absolute;left:55px;top:26px;width:186px;height:156px;background:radial-gradient(ellipse at center,rgba(236,170,50,.55) 0%,rgba(190,60,40,.25) 55%,rgba(38,40,43,0) 72%)}
.order-today{position:absolute;left:0;width:326px;top:200px;font-size:24px;font-weight:300}
.ships{position:absolute;left:0;width:326px;top:230px;font-size:26px;font-weight:800;color:var(--orange)}
.by5{position:absolute;left:0;width:326px;top:262px;font-size:20px;font-weight:300;color:var(--sky);line-height:26px}
.cutoff{position:absolute;left:0;width:326px;top:292px;font-size:11px;font-style:italic}
.view-btn{position:absolute;left:42px;top:315px;width:240px;height:48px;background:var(--orange);color:#7a1d00;font-weight:700;font-size:17px;line-height:48px}
.dots{position:absolute;right:22px;top:372px;display:flex;gap:5px}
.dots i{width:8px;height:8px;border-radius:50%;background:#aaa}
.dots i:first-child{background:var(--sky)}

/* config bar */
.configbar{left:99px;top:502px;width:1002px;height:73px;border:1px solid var(--line);border-top:none}
.lbl{position:absolute;color:var(--blue);font-weight:700;text-transform:uppercase;font-size:12px;top:27px}
.sel{position:absolute;top:20px;height:32px;border:1px solid #ccc;background:#fff;font-size:9px;color:#999;padding-left:9px;line-height:30px;text-transform:uppercase}
.sel::after{content:"";position:absolute;right:9px;top:12px;border:5px solid transparent;border-top-color:#666}
.price-each{position:absolute;left:744px;top:27px;color:#888;font-size:12px}
.price-each b{color:var(--orange);font-size:17px;font-weight:700}
.start-btn{position:absolute;left:873px;top:18px;width:111px;height:30px;background:var(--orange);color:#fff;font-size:10px;font-weight:700;text-align:center;line-height:30px}
.upload-link{position:absolute;left:873px;top:52px;width:111px;text-align:center;font-size:9.5px;font-weight:600;color:var(--blue);display:flex;gap:4px;justify-content:center;align-items:center}

/* categories */
.cats{left:99px;top:602px;width:254px;height:924px;border:1px solid var(--line)}
.cats h3{height:41px;background:linear-gradient(#1a6bbd,var(--blue));color:#fff;font-size:13px;font-weight:700;padding-left:20px;line-height:41px;margin:-1px -1px 0}
.cats ul{list-style:none;padding:11px 0 0 21px}
.cats li{font-size:11px;height:26.6px;line-height:26.6px;color:#555}
.cats li::before{content:"›";color:var(--orange);margin-right:9px;font-weight:700}

/* featured */
.sec-title{color:var(--blue);font-weight:700;font-size:14px;text-transform:uppercase}
.feat-title{left:395px;top:613px;width:706px;padding-bottom:10px;border-bottom:1px solid var(--line)}
.product{position:absolute;width:221px}
.product .ph{height:148px}
.product p{text-align:center;font-size:11.5px;font-weight:700;color:#333;margin-top:10px}
.pager{left:714px;top:1256px;display:flex;gap:6px}
.pager span{height:25px;min-width:25px;padding:0 8px;border:1px solid #ccc;background:#f3f3f3;font-size:11px;line-height:23px;text-align:center}

/* discounts */
.disc-title{left:395px;top:1309px;font-size:13px}
.disc-box{left:395px;top:1348px;width:233px;height:178px;background:var(--sky);color:#fff;text-align:center}
.disc-box h4{font-size:14px;font-weight:600;margin-top:22px}
.disc-sel{position:absolute;left:20px;top:56px;width:187px;height:30px;background:#fff;color:#666;font-size:10px;line-height:30px;text-align:left;padding-left:10px}
.disc-sel::after{content:"⌄";position:absolute;right:10px;top:-3px}
.ship-btn{position:absolute;left:20px;top:96px;width:187px;height:33px;background:var(--blue);font-size:12px;font-weight:700;line-height:33px}
.quotes{position:absolute;left:20px;top:142px;font-size:12px}
.disc-table{left:628px;top:1348px;width:473px;height:178px;border-collapse:collapse;font-size:11px}
.disc-table th{background:var(--blue);color:#fff;height:36px;text-align:left;padding-left:12px;font-weight:600;border-right:1px solid #fff}
.disc-table td{height:35.5px;padding-left:12px;color:#888;border-bottom:1px solid #fff;border-right:1px solid var(--line)}
.disc-table tr:nth-child(even) td{background:var(--row-alt)}
.disc-table tr:nth-child(odd) td{background:#fff}

/* search dropdowns */
.finder{left:99px;top:1572px;width:1002px;display:flex;justify-content:space-between}
.finder div{width:236px;position:relative}
.finder label{display:block;color:var(--blue);font-size:11px;font-weight:600;margin-bottom:10px}
.finder .box{height:30px;border:1px solid #bbb;font-size:10px;color:#999;line-height:28px;padding-left:10px;position:relative}
.finder .box::after{content:"";position:absolute;right:10px;top:11px;border:5px solid transparent;border-top-color:#555}
.rule{left:99px;top:1662px;width:1002px;height:1px;background:var(--line)}
.lib-title{left:99px;top:1688px;font-size:16px}
.lib-col{position:absolute;top:1728px;list-style:none;font-size:11px;color:#555}
.lib-col li{height:24px}

/* news band */
.band{left:0;top:1887px;width:1200px;height:333px;background:var(--gray-band)}
.band-title{font-size:16px}
.arrows{color:#999;font-size:13px}
.post-title{left:99px;top:1978px;width:260px;color:var(--sky);font-size:12px;font-weight:700;line-height:22px;text-transform:uppercase}
.post-date{left:99px;top:2029px;font-size:10px;color:#777}
.post-body{left:99px;top:2050px;width:300px;font-size:11px;line-height:23px;color:#555}
.offer{left:447px;top:1945px;width:314px;height:210px;background:linear-gradient(135deg,#d9c4a8,#b58c6a 45%,#4e5c6e);overflow:hidden}
.offer h5{position:absolute;left:20px;top:143px;color:var(--orange);font-size:18px;font-weight:700}
.offer p{position:absolute;left:20px;top:168px;color:#fff;font-size:13px;font-weight:700}
.quote{left:826px;top:1984px;width:260px;font-size:11px;line-height:23.5px;color:#555}
.qmark{color:#aaa;font-size:28px;font-family:Georgia,serif;position:absolute}
.avatar{left:826px;top:2090px;width:66px;height:62px;background:linear-gradient(#c9b49a,#8e7b68);border:3px solid #fff}
.t-name{left:915px;top:2099px;color:var(--sky);font-size:12px;font-weight:700;text-transform:uppercase}
.t-role{left:915px;top:2122px;color:#888;font-size:10px;text-transform:uppercase}

/* footer */
.footer{left:0;top:2220px;width:1200px;height:205px;background:var(--blue);color:#fff}
.fcol{position:absolute;top:44px;width:128px}
.fcol h6{font-size:11px;font-weight:700;text-transform:uppercase;padding-bottom:9px;border-bottom:1px solid rgba(255,255,255,.8);margin-bottom:10px}
.fcol li{list-style:none;font-size:11px;height:23px}
.subfoot{left:0;top:2425px;width:1200px;height:41px;background:var(--pale);font-size:9.5px;color:#556;text-transform:uppercase}
.subfoot .copy{position:absolute;left:99px;top:14px;letter-spacing:.3px}
.subfoot .social{position:absolute;left:740px;top:12px;display:flex;gap:12px;align-items:center}
.subfoot .social i{width:16px;height:16px;border-radius:50%;background:var(--blue);display:block}
</style>
</head>
<body>

<header>
  <div class="abs topbar"></div>
  <div class="abs brand">LAWNMARK</div>
  <div class="abs search-btn"><svg width="17" height="17" viewBox="0 0 17 17"><circle cx="7" cy="7" r="5" fill="none" stroke="#fff" stroke-width="2"/><line x1="11" y1="11" x2="15" y2="15" stroke="#fff" stroke-width="2"/></svg></div>
  <nav class="abs user-nav"><span>My Account</span><span>My Cart</span><span>Login</span><span>Register</span></nav>
  <div class="abs cart"><svg width="16" height="14" viewBox="0 0 16 14"><path d="M0 1h3l2 8h9l2-6H4" fill="none" stroke="#fff" stroke-width="1.5"/><circle cx="6" cy="12" r="1.5" fill="#fff"/><circle cx="13" cy="12" r="1.5" fill="#fff"/></svg>Your cart is : 0 Items</div>
  <nav class="abs mainnav"><ul><li>Banners</li><li>Aluminum</li><li>Yard Signs</li><li>Rigid Plastic</li><li>Acrylic</li><li>Foam Board</li><li>Window Decals</li><li>More</li></ul></nav>
</header>

<section class="abs hero">
  <div class="hero-photo" role="img" aria-label="Photo of a red for-sale sign hanging on a post in front of a house"></div>
  <div class="hero-copy">
    <div class="seal" role="img" aria-label="Money back guarantee seal"></div>
    <div class="order-today">ORDER TODAY</div>
    <div class="ships">SHIPS TOMORROW</div>
    <div class="by5">ORDER BY 5PM EST</div>
    <div class="cutoff">16 hours &amp; 35 minutes until next cut off</div>
    <a class="view-btn">VIEW DETAILS</a>
  </div>
  <div class="dots"><i></i><i></i><i></i><i></i></div>
</section>

<div class="abs configbar">
  <span class="lbl" style="left:16px">Sign Type</span>
  <span class="sel" style="left:93px;width:191px">Banner</span>
  <span class="lbl" style="left:304px">Size (Inches)</span>
  <span class="sel" style="left:397px;width:81px">Width</span>
  <span class="sel" style="left:488px;width:80px">Height</span>
  <span class="lbl" style="left:583px">Quantity</span>
  <span class="sel" style="left:661px;width:70px">Pcs</span>
  <span class="price-each">Price each: <b>$48.52</b></span>
  <a class="start-btn">GET STARTED</a>
  <a class="upload-link"><svg width="9" height="9" viewBox="0 0 9 9"><path d="M4.5 7V1M2 3.5l2.5-2.5L7 3.5M1 8h7" fill="none" stroke="#0455a3" stroke-width="1.3"/></svg>Upload your design</a>
</div>

<aside class="abs cats">
  <h3>CATEGORIES</h3>
  <ul>
    <li>Banners</li><li>Aluminum Signs</li><li>Yard Signs</li><li>Rigid Plastic</li><li>Acrylic Signs</li><li>Foam Board</li><li>Clear Window Decal</li><li>Opaque Window Decal</li><li>Perforated Window Decal</li><li>Frosted Window Decal</li><li>Magnets</li><li>Brushed Aluminum</li><li>Wall Decals</li><li>Clear Static Cling</li><li>Clear Car Decal</li><li>Opaque Car Decal</li><li>Perforated Car Decal</li><li>Wooden Sign</li><li>High Adhesive Decal</li><li>Floor Decals</li><li>Backlit Decals</li><li>Poster</li><li>Opaque Static Cling</li><li>Fabric Banner</li><li>Vinyl Lettering</li><li>Canvas Prints</li><li>Falconboard</li><li>A-Frame Signs</li><li>Retractable Banners</li><li>Glossy Photo Print</li><li>Matte Photo Print</li><li>Glossy Photo Print</li>
  </ul>
</aside>

<h2 class="abs sec-title feat-title">Featured Products</h2>

<div class="product" style="left:395px;top:663px"><div class="ph" role="img" aria-label="For sale sign in front of a house" style="background:linear-gradient(135deg,#8a9aa8,#e8e4dc 50%,#c8283a)"></div><p>BANNERS</p></div>
<div class="product" style="left:638px;top:663px"><div class="ph" role="img" aria-label="Green exit sign on a ceiling" style="background:linear-gradient(135deg,#cfd4d2,#eef0ee 50%,#9ea6a3)"></div><p>ALUMINUM SIGNS</p></div>
<div class="product" style="left:880px;top:663px"><div class="ph" role="img" aria-label="Yellow pedestrian warning sign against the sky" style="background:linear-gradient(135deg,#9bb6d8,#e9c21a 50%,#c7d6ea)"></div><p>YARD SIGNS</p></div>
<div class="product" style="left:395px;top:853px"><div class="ph" role="img" aria-label="Crazy sale lettering on yellow" style="background:linear-gradient(135deg,#f3c300,#f7a400 50%,#d8231d)"></div><p>BANNERS</p></div>
<div class="product" style="left:638px;top:853px"><div class="ph" role="img" aria-label="Green street sign reading success way" style="background:linear-gradient(135deg,#6f9fd6,#2d8a4a 50%,#b8d0ec)"></div><p>ALUMINUM SIGNS</p></div>
<div class="product" style="left:880px;top:853px"><div class="ph" role="img" aria-label="Green airport direction sign" style="background:linear-gradient(135deg,#27b7ea,#1c8b3f 50%,#27b7ea)"></div><p>YARD SIGNS</p></div>
<div class="product" style="left:395px;top:1046px"><div class="ph" role="img" aria-label="Road closed and diversion signs on a street" style="background:linear-gradient(135deg,#c9c6c0,#808080 50%,#e8b02a)"></div><p>BANNERS</p></div>
<div class="product" style="left:638px;top:1046px"><div class="ph" role="img" aria-label="Airport terminal gates direction sign" style="background:linear-gradient(135deg,#9a9da0,#2a2f36 50%,#6d7278)"></div><p>ALUMINUM SIGNS</p></div>
<div class="product" style="left:880px;top:1046px"><div class="ph" role="img" aria-label="Challenges ahead yellow road sign against clouds" style="background:linear-gradient(135deg,#2e5f9e,#e8b81c 50%,#7fa2cc)"></div><p>YARD SIGNS</p></div>

<div class="abs pager"><span>Prev</span><span>1</span><span>2</span><span>3</span><span>4</span><span>5</span><span>6</span><span>...</span><span>22</span><span>Next</span></div>

<h2 class="abs sec-title disc-title">Quantity Discounts Apply To Exact Designs Only</h2>
<div class="abs disc-box">
  <h4>SELECT SIZE (HXW)</h4>
  <div class="disc-sel">18"X24" 1-Sided</div>
  <a class="ship-btn">GET FREE SHIPPING</a>
  <span class="quotes">Print Quotes</span>
</div>
<table class="abs disc-table">
  <tr><th style="width:107px">Qty Discounts</th><th>1</th><th>5+</th><th>10+</th><th>25+</th><th>50+</th></tr>
  <tr><td>Price each</td><td>$15.99</td><td>$11.83</td><td>$10.93</td><td>$8.63</td><td>$7.84</td></tr>
  <tr><td>Price each</td><td>$15.99</td><td>$11.83</td><td>$10.93</td><td>$8.63</td><td>$7.84</td></tr>
  <tr><td>Price each</td><td>$15.99</td><td>$11.83</td><td>$10.93</td><td>$8.63</td><td>$7.84</td></tr>
  <tr><td>Price each</td><td>$15.99</td><td>$11.83</td><td>$10.93</td><td>$8.63</td><td>$7.84</td></tr>
</table>

<div class="abs finder">
  <div><label>Search By Sign Type</label><div class="box">- Select -</div></div>
  <div><label>Search By Sign Category</label><div class="box">- Select -</div></div>
  <div><label>Search By Sign Industry</label><div class="box">- Select -</div></div>
  <div><label>Search By Sign Material</label><div class="box">- Select -</div></div>
</div>
<div class="abs rule"></div>

<h2 class="abs sec-title lib-title">Search Our Template Library</h2>
<ul class="lib-col" style="left:99px"><li>Business</li><li>Events</li><li>Business Hours</li><li>Real Estate</li><li>Holidays</li></ul>
<ul class="lib-col" style="left:252px"><li>Traffic</li><li>Residential</li><li>Animals</li><li>Safety</li><li>Birthday</li></ul>
<ul class="lib-col" style="left:398px"><li>School</li><li>Sports</li><li>Sale</li><li>Safety &amp; Regulation</li><li>Military</li></ul>
<ul class="lib-col" style="left:587px"><li>Directional</li><li>Food &amp; Beverage</li><li>Restroom</li><li>Opening</li><li>Parking</li></ul>
<ul class="lib-col" style="left:784px"><li>Now Hiring</li><li>Construction</li><li>Trade</li><li>Welcome</li><li>Wedding</li></ul>
<ul class="lib-col" style="left:963px"><li>Welcome Home</li><li>Salon &amp; Spa</li><li>Anniversary</li><li>Government</li><li>Yard Sale</li></ul>

<section class="abs band"></section>
<h2 class="abs sec-title band-title" style="left:99px;top:1941px">Latest Posts</h2>
<span class="abs arrows" style="left:378px;top:1940px">‹ ›</span>
<h3 class="abs post-title">Lorem Ipsum Is Simply Dummy Text Of The Printing</h3>
<div class="abs post-date">POSTED ON 28 MARCH 2015</div>
<p class="abs post-body">Lorem Ipsum is simply dummy text of the printing and typesetting industry. Lorem Ipsum has been the industry's standard dummy text ever since the 1500s, when an unknown printer took a galley of type and scrambled it to make a type specimen book...</p>

<div class="abs offer" role="img" aria-label="Shop owner holding an open sign">
  <h5>OFFER PRODUCTS</h5>
  <p>LOREM IPSUM IS SIMPLY DUMMY TEXT</p>
</div>

<h2 class="abs sec-title band-title" style="left:801px;top:1941px">Testimonials</h2>
<span class="abs arrows" style="left:1078px;top:1940px">‹ ›</span>
<span class="qmark" style="left:801px;top:1976px">“</span>
<p class="abs quote">Lorem Ipsum is simply dummy text of the printing and typesetting industry. Lorem Ipsum has been the industry's standard dummy text ever since the 1500s, when an unknown...</p>
<span class="qmark" style="left:1090px;top:2040px">”</span>
<div class="abs avatar" role="img" aria-label="Portrait of the customer"></div>
<div class="abs t-name">Marlo Tesk</div>
<div class="abs t-role">Business Man</div>

<footer class="abs footer">
  <div class="fcol" style="left:99px"><h6>Products</h6><ul><li>About</li><li>News</li><li>Policies</li><li>Our Advantage</li></ul></div>
  <div class="fcol" style="left:304px"><h6>Resources</h6><ul><li>FAQ</li><li>Design Services</li><li>Giving Back</li><li>Site Map</li></ul></div>
  <div class="fcol" style="left:510px"><h6>Support</h6><ul><li>Contact Us</li><li>How Tos</li><li>Careers</li></ul></div>
  <div class="fcol" style="left:723px"><h6>Shop</h6><ul><li>Sign Types</li><li>Templates</li><li>Price Calculator</li></ul></div>
  <div class="fcol" style="left:929px"><h6>Information</h6><ul><li>Terms &amp; Conditions</li><li>Privacy Policy</li><li>Disclaimer</li><li>Sitemap</li></ul></div>
</footer>
<div class="abs subfoot">
  <span class="copy">Copyright © 2015 Lawnmark. All rights reserved.</span>
  <div class="social"><span>Connect with our social network :</span><i></i><i></i><i></i><i></i><i></i></div>
</div>

</body>
</html>
```